Four banner campaigns, much work to come!

I want banners created for 4 campaigns.

For each campaign I need these 6 banner sizes created:

? Web Banner Sizes (300x250, 728x90, 160x600)
One of each of these sizes, so 3 web banners

? Mobile Banner Sizes (300x50, 216x36, 240x240)

Campaign 1
http://www.cornerfirmratings.example/KLV-40275.html

Campaign 2
http://www.cornerfirmratings.example/Rockville-MD/Velunor-38412.html

Campaign 3
http://www.townlistingpages.example/m/orlando-fl-vacation-rentals/

Campaign 4
www.cornerfirmratings.example/The-Wexbridge-Institute-of-Sound-and-Screen-Studies-40269.html

I will send you numbers to edit each banner, so the 24 banners
will have 4 variations with different numbers. Same banners just
need you to send a copy with different phone numbers.

I want the work done today and I will post my next gig for the same winner.
Updates

I just want to make sure everyone knows this project is for 4 different banner campaigns.

Given banners in each size for each campaign.  I can submit additional info links if
needed let me know.  Please post more samples as soon as possible so I can pick
a designer to finish.

Thank you!

Industry/Entity Type

Radio

Requirements
Must have
• Messaging that follows the messaging in the pages I have submitted.
Nice to have
• Animated gif banners in general, QMV compliant.

```html
<!DOCTYPE html>
<html lang="en">
<head>
<meta charset="utf-8">
<title>Harbor Stay Villas – Banner Set</title>
<link rel="stylesheet" href="https://fonts.googleapis.com/css2?family=Arimo:wght@400;700&display=swap">
<style>
  :root {
    --backdrop-dark: #2a2a2a;
    --backdrop-light: #5a5a5a;
    --frame: #06070a;
    --panel: #ffffff;
    --header-band: #dcdcdc;
    --ink: #000000;
    --phone: #8e9bbd;
    --mark: #8e9bbd;
    --sky: #3f86d8;
    --palm: #4f7d2c;
    --lawn: #5d9b34;
    --stone: #c9b08a;
    --terrace: #d9d6cf;
    --cushion: #c8161c;
  }
  * { box-sizing: border-box; margin: 0; padding: 0; }
  html, body { width: 1200px; height: 1080px; overflow: hidden; }
  body {
    font-family: "Arimo", Arial, sans-serif;
    background:
      repeating-linear-gradient(100deg, rgba(255,255,255,0.05) 0 6px, rgba(0,0,0,0.08) 6px 14px, rgba(255,255,255,0.03) 14px 22px),
      radial-gradient(ellipse at 40% 30%, var(--backdrop-light), var(--backdrop-dark) 75%);
  }
  .stage {
    position: relative;
    width: 1000px; height: 900px;
    transform: scale(1.2);
    transform-origin: 0 0;
  }
  .banner { position: absolute; background: var(--frame); }
  .photo { position: absolute; }
  .photo--fountain { background: linear-gradient(180deg, var(--sky) 0%, #7fb4e6 35%, var(--palm) 60%, var(--stone) 80%, var(--lawn) 100%); }
  .photo--residence { background: linear-gradient(180deg, #4c8fdc 0%, #a8c7e6 30%, #f0ece4 48%, var(--palm) 62%, var(--lawn) 100%); }
  .photo--terrace { background: linear-gradient(180deg, #8fb8d8 0%, var(--terrace) 35%, var(--cushion) 60%, #9c2020 75%, var(--terrace) 100%); }

  .panel {
    position: absolute;
    background: var(--panel);
    border-radius: 8px;
    overflow: hidden;
    text-align: center;
    color: var(--ink);
  }
  .panel__header {
    background: var(--header-band);
    font-weight: 700;
    display: flex; align-items: center; justify-content: center;
  }
  .brand {
    display: flex; align-items: center; gap: 4px;
    font-weight: 700; color: var(--ink); white-space: nowrap;
  }
  .brand__dot { border-radius: 50%; background: var(--mark); flex: none; }
  .cta { font-weight: 700; line-height: 1.05; }
  .cta__phone { color: var(--phone); display: block; }

  /* 728x90 leaderboard */
  .banner--leaderboard { left: 138px; top: 88px; width: 727px; height: 90px; }
  .banner--leaderboard .panel { left: 429px; top: 4px; width: 294px; height: 82px; }
  .banner--leaderboard .panel__header { height: 26px; font-size: 15px; }
  .banner--leaderboard .panel__body { display: flex; align-items: center; justify-content: space-between; padding: 6px 14px 0 18px; }
  .banner--leaderboard .brand { font-size: 17px; }
  .banner--leaderboard .brand__dot { width: 22px; height: 22px; }
  .banner--leaderboard .cta { font-size: 13px; }
  .banner--leaderboard .cta__phone { font-size: 17px; }

  /* 300x250 rectangle */
  .banner--rectangle { left: 352px; top: 214px; width: 299px; height: 249px; }
  .banner--rectangle .panel { left: 3px; top: 5px; width: 293px; height: 133px; }
  .banner--rectangle .panel__header { height: 43px; font-size: 15.5px; }
  .banner--rectangle .panel__body { display: flex; align-items: center; justify-content: space-between; padding: 22px 18px 0 16px; }
  .banner--rectangle .brand { font-size: 17px; }
  .banner--rectangle .brand__dot { width: 22px; height: 22px; }
  .banner--rectangle .cta { font-size: 13.5px; }
  .banner--rectangle .cta__phone { font-size: 18px; }

  /* 160x600 skyscraper */
  .banner--skyscraper { left: 705px; top: 214px; width: 160px; height: 599px; }
  .banner--skyscraper .panel { left: 5px; top: 5px; width: 150px; height: 338px; padding-top: 36px; }
  .banner--skyscraper .brand { justify-content: center; font-size: 20px; }
  .banner--skyscraper .brand__dot { width: 26px; height: 26px; }
  .banner--skyscraper .panel__lead { margin-top: 38px; font-weight: 700; font-size: 16px; line-height: 1.3; }
  .banner--skyscraper .panel__lead span { font-size: 19px; }
  .banner--skyscraper .cta { margin-top: 30px; font-size: 21px; line-height: 1.2; }
  .banner--skyscraper .cta__phone { font-size: 32px; line-height: 1.55; margin-top: 2px; }
</style>
</head>
<body>
<main class="stage">

  <section class="banner banner--leaderboard" aria-label="728 by 90 banner">
    <div class="photo photo--fountain" style="left:2px;top:2px;width:141px;height:86px" role="img" aria-label="Photo of a tiered stone fountain among palm trees"></div>
    <div class="photo photo--residence" style="left:145px;top:2px;width:139px;height:86px" role="img" aria-label="Photo of a resort residence with a curving driveway and lawn"></div>
    <div class="photo photo--terrace" style="left:287px;top:2px;width:138px;height:86px" role="img" aria-label="Photo of a balcony terrace with red outdoor sofas"></div>
    <div class="panel">
      <div class="panel__header">Reserve a home today</div>
      <div class="panel__body">
        <div class="brand"><span class="brand__dot"></span>Harbor Stay</div>
        <div class="cta">Give us a call at<span class="cta__phone">(888) 555-0142</span></div>
      </div>
    </div>
  </section>

  <section class="banner banner--rectangle" aria-label="300 by 250 banner">
    <div class="panel">
      <div class="panel__header">Reserve a home today</div>
      <div class="panel__body">
        <div class="brand"><span class="brand__dot"></span>Harbor Stay</div>
        <div class="cta">Give us a call at<span class="cta__phone">(888) 555-0142</span></div>
      </div>
    </div>
    <div class="photo photo--fountain" style="left:3px;top:147px;width:142px;height:100px" role="img" aria-label="Photo of a tiered stone fountain among palm trees"></div>
    <div class="photo photo--residence" style="left:148px;top:147px;width:148px;height:100px" role="img" aria-label="Photo of a resort residence with a curving driveway and lawn"></div>
  </section>

  <section class="banner banner--skyscraper" aria-label="160 by 600 banner">
    <div class="panel">
      <div class="brand"><span class="brand__dot"></span>Harbor Stay</div>
      <p class="panel__lead">Reserve a home<br><span>today</span></p>
      <div class="cta">Give us a<br>call at<span class="cta__phone">(888)<br>555-0142</span></div>
    </div>
    <div class="photo photo--fountain" style="left:3px;top:366px;width:152px;height:96px" role="img" aria-label="Photo of a tiered stone fountain among palm trees"></div>
    <div class="photo photo--terrace" style="left:3px;top:483px;width:152px;height:95px" role="img" aria-label="Photo of a balcony terrace with red outdoor sofas"></div>
  </section>

</main>
</body>
</html>
```